Brightfern Couples Unity Program

We need a flyer that invites low-income Spanish speaking individuals to our program. The program is 12 weeks. We offer healthy relationship education, and financial stability. We also touch on workforce development. These workshops are for couples only.

We are in five locations, so we need a flyer that we can change the text to be able to update the address, dates and any additional information based on our needs.

Attached is the logo we would like to use. I have also attached a previous flyer that we created to give you an idea of the text that is included.

Target Market(s)

We are reaching out to low income adult couples

Font styles to use
Serif

Requirements
Must have
• This flyer must catch the eye of couples wanting to improve their relationship, and finances.
Nice to have
• Some space for us to plug in dates location and times. This flyer also has to have our funding statement at the bottom.

```html
<!DOCTYPE html>
<html lang="es">
<head>
<meta charset="utf-8">
<title>Brightfern Couples Unity Program – Talleres para Parejas</title>
<link rel="stylesheet" href="https://fonts.googleapis.com/css2?family=Questrial&family=Alegreya+SC:wght@700&family=Playfair+Display:wght@900&family=Dancing+Script:wght@500&family=Bitter:ital,wght@0,400;0,700;1,400&family=PT+Serif:ital,wght@0,400;0,700;1,400&display=swap">
<style>
  :root {
    --navy: #0f3a5c;
    --frame-light: #0d5a7e;
    --frame-dark: #0a1a33;
    --orange: #f7820f;
    --orange-band: #ff8000;
    --ink: #111111;
    --white: #ffffff;
    --green: #3a9a2a;
    --red: #d42a1c;
    --maroon: #9b1b3a;
    --blue: #1f3fa8;
  }
  * { margin: 0; padding: 0; box-sizing: border-box; }
  html, body { width: 849px; height: 1200px; overflow: hidden; }
  body {
    background: linear-gradient(135deg, var(--frame-light) 0%, #0c3f66 45%, var(--frame-dark) 100%);
    font-family: "PT Serif", Georgia, serif;
    color: var(--ink);
    position: relative;
  }
  .flyer {
    position: absolute;
    left: 40px; top: 40px;
    width: 768px; height: 1120px;
    background: var(--white);
  }
  .program-name {
    position: absolute;
    left: 0; right: 0; top: 178px;
    text-align: center;
    font-family: "Questrial", Arial, sans-serif;
    font-weight: 400;
    font-size: 42px;
    line-height: 56px;
    white-space: nowrap;
    color: var(--orange);
  }
  .name-rule {
    position: absolute;
    top: 244px;
    height: 2px;
  }
  .name-rule.left { left: 20px; width: 328px; background: var(--orange); }
  .name-rule.right { left: 380px; width: 368px; background: var(--navy); }
  .services {
    position: absolute;
    left: 0; right: 0; top: 252px;
    text-align: center;
    font-family: "Alegreya SC", Georgia, serif;
    font-weight: 700;
    font-size: 25px;
    line-height: 34px;
    color: var(--navy);
  }
  .headline {
    position: absolute;
    left: 40px; top: 340px;
    width: 688px; height: 174px;
  }
  .headline text {
    font-family: "Playfair Display", "Times New Roman", serif;
    font-weight: 900;
    fill: url(#headlineInk);
  }
  .tagline {
    position: absolute;
    left: 0; right: 0; top: 532px;
    text-align: center;
    font-family: "Dancing Script", cursive;
    font-size: 25px;
    line-height: 34px;
    color: var(--ink);
  }
  .details-band {
    position: absolute;
    left: 0; top: 582px;
    width: 768px; height: 152px;
    background: var(--orange-band);
    font-family: "Bitter", Georgia, serif;
    text-align: center;
    padding-top: 12px;
  }
  .details-band p { font-size: 31px; line-height: 45px; white-space: nowrap; }
  .details-band .label { font-weight: 700; color: var(--ink); }
  .details-band .value { font-style: italic; font-weight: 400; }
  .topics {
    position: absolute;
    left: 13px; top: 756px;
    width: 380px;
    font-size: 14.5px;
    line-height: 20px;
  }
  .topics ul { list-style: none; margin-top: 1px; }
  .topics li { padding-left: 24px; position: relative; }
  .topics li::before {
    content: "";
    position: absolute; left: 6px; top: 6px;
    border-left: 6px solid var(--ink);
    border-top: 4px solid transparent;
    border-bottom: 4px solid transparent;
  }
  .column-rule {
    position: absolute;
    left: 400px; top: 756px;
    width: 1px; height: 178px;
    background: var(--ink);
  }
  .contact {
    position: absolute;
    left: 421px; top: 750px;
    width: 340px;
    font-size: 14px;
    line-height: 20px;
  }
  .contact .phone { font-size: 19px; font-weight: 700; line-height: 26px; }
  .contact .note { color: var(--orange); font-weight: 700; font-size: 13px; line-height: 16px; }
  .contact .call { font-size: 23px; font-weight: 700; line-height: 31px; margin-top: 8px; }
  .contact .info { font-size: 15.5px; line-height: 20px; }
  .footer-rule {
    position: absolute;
    left: 10px; top: 952px;
    width: 748px; height: 1px;
    background: #444;
  }
  .partner {
    position: absolute;
    display: flex; align-items: center; gap: 8px;
    font-family: "PT Serif", Georgia, serif;
    font-weight: 700;
    font-size: 13px;
    line-height: 16px;
  }
  .partner.resource-center { left: 408px; top: 1010px; width: 200px; color: var(--red); }
  .partner.resource-center .dot { width: 20px; height: 20px; border-radius: 50%; background: var(--green); flex: none; }
  .partner.community { left: 626px; top: 1002px; width: 130px; color: var(--blue); }
  .partner.community .dot { width: 20px; height: 20px; background: var(--maroon); flex: none; }
  .funding {
    position: absolute;
    left: 14px; top: 1078px;
    width: 744px;
    font-style: italic;
    font-size: 11.6px;
    line-height: 17px;
  }
</style>
</head>
<body>
  <main class="flyer">
    <h1 class="program-name">Brightfern Couples Unity Program</h1>
    <div class="name-rule left"></div>
    <div class="name-rule right"></div>

    <p class="services">Fortalecimiento de Relaciones | Capacitación Financiera<br>y Preparación Laboral</p>

    <svg class="headline" viewBox="0 0 688 174" aria-label="Talleres para parejas">
      <defs>
        <linearGradient id="headlineInk" x1="0" y1="0" x2="0" y2="1">
          <stop offset="0" stop-color="#1a4e74"/>
          <stop offset="1" stop-color="#081c30"/>
        </linearGradient>
      </defs>
      <text x="0" y="92" font-size="127" textLength="688" lengthAdjust="spacingAndGlyphs">TALLERES</text>
      <text x="0" y="172" font-size="96" textLength="688" lengthAdjust="spacingAndGlyphs">PARA PAREJAS</text>
    </svg>

    <p class="tagline">Porque una relación sana esta · “A Nuestro Alcance”</p>

    <section class="details-band">
      <p><span class="label">Fecha de talleres:</span> <span class="value">Jueves octubre 03, 12, 19, 26</span></p>
      <p><span class="label">Horario:</span> <span class="value">5:30pm –8:00pm</span></p>
      <p><span class="label">Ubicación:</span> <span class="value">Alderbrook Family Resource Center</span></p>
    </section>

    <section class="topics">
      <p>Temas incluyen:</p>
      <ul>
        <li>Llaves para la buena communicación</li>
        <li>Tipos de personalidad y expectativas</li>
        <li>Señales de peligro en una relación</li>
        <li>Técnicas para formar y sostener una relación sana</li>
        <li>Resolucion de problemas</li>
        <li>Como mantener la diversion</li>
        <li>Como adminstrar el dinero entre pareja</li>
        <li>Y muchos mas</li>
      </ul>
    </section>

    <div class="column-rule"></div>

    <section class="contact">
      <p>4820 Larkspur Ave, Westhaven CA 90417</p>
      <p class="phone">(555) 214-3860</p>
      <p class="note">*Cuidado de niños y cena será proporcionado</p>
      <p class="call">Registración requerida<br>Llámanos hoy!</p>
      <p class="info">Para más información llame a<br>Alderbrook Family Resource Center</p>
      <p class="phone">(555) 214-3972</p>
    </section>

    <div class="footer-rule"></div>

    <div class="partner resource-center"><span class="dot"></span><span>ALDERBROOK<br>FAMILY RESOURCE CENTER</span></div>
    <div class="partner community"><span class="dot"></span><span>Riverstone<br>Community<br>Partners</span></div>

    <p class="funding">“Funding for this project was provided by the Northvale Department of Family Services, Office for Children and Families, Grant: #91BC2247.  These services are available to all eligible persons, regardless of race, gender, age, disability, or religion.”</p>
  </main>
</body>
</html>
```